Waterproofing Construction company needs letterhead

I need a letterhead design for a commercial waterproofing construction company. We would like to see designs that are contemporary, clean, sleek and use our logo. Our current design is dated. I would also like a cover page (see example) that goes with our letterhead. I would like for the footer to have our address, website, and phone number

Target Market(s)

Customers, potential customers.

Font styles to use
Sans Serif

Requirements
Must have
• logo, website, address, phone numbers, only our colors, tahoma font
• PMS: 295C PMS: 2995C
• CMYK: 100/84/36/39 CMYK: 80/12/1/0
• RGB: 16/44/82 RGB: 0/167/224
• HEX#: #102C52 HEX#: #00A7E0
• Black & White: 100% Black & White: 32%
• Gray Scale: 90% Gray Scale: 32%
Nice to have
• Our "icon" logo attached would be nice somewhere on the page.

```html
<!DOCTYPE html>
<html lang="en">
<head>
<meta charset="utf-8">
<title>Keystone Seal Letterhead</title>
<link rel="stylesheet" href="https://fonts.googleapis.com/css2?family=Noto+Sans:wght@400;700;800&display=swap">
<style>
  :root {
    --navy: #102C52;
    --cyan: #00A7E0;
    --blue-mid: #2f7fd6;
    --ink: #555b63;
    --paper: #ffffff;
    --backdrop: #9cc3ea;
  }
  html, body {
    margin: 0;
    width: 1200px;
    height: 784px;
    overflow: hidden;
    background: var(--backdrop);
    font-family: "Noto Sans", Tahoma, sans-serif;
  }
  .letterhead {
    position: absolute;
    left: 335px;
    top: 17px;
    width: 530px;
    height: 750px;
    background: var(--paper);
    overflow: hidden;
    box-shadow: 0 6px 24px rgba(16, 44, 82, 0.18);
  }
  .corner {
    position: absolute;
    display: block;
  }
  .corner--top { top: 0; right: 0; }
  .corner--bottom { bottom: 0; left: 0; }
  .brand {
    position: absolute;
    top: 46px;
    right: 44px;
    display: flex;
    align-items: center;
    gap: 8px;
  }
  .brand__name {
    font-weight: 800;
    font-size: 24px;
    letter-spacing: -0.5px;
    color: var(--navy);
    line-height: 1;
  }
  .brand__mark {
    width: 14px;
    height: 14px;
    background: var(--cyan);
  }
  .letter {
    position: absolute;
    top: 118px;
    left: 62px;
    right: 56px;
    color: var(--ink);
    font-size: 8.2px;
    line-height: 1.55;
  }
  .letter p { margin: 0 0 11px; text-indent: 22px; }
  .letter p:first-child { margin-left: 48px; }
  .signature {
    display: block;
    margin-top: 14px;
    width: 130px;
    height: 38px;
    background: linear-gradient(90deg, #e9ebee, #f4f5f6);
    border-radius: 3px;
  }
  .contact {
    position: absolute;
    left: 30px;
    right: 30px;
    bottom: 30px;
    display: flex;
    flex-wrap: wrap;
    gap: 4px 14px;
    font-size: 8px;
    color: var(--navy);
  }
  .contact__item { display: flex; align-items: center; gap: 4px; }
  .contact__icon { width: 9px; height: 9px; flex: none; }
</style>
</head>
<body>
<main class="letterhead">
  <svg class="corner corner--top" width="170" height="120" viewBox="0 0 170 120" aria-hidden="true">
    <path d="M40 0 H170 V120 Z" fill="var(--navy)"/>
    <path d="M0 0 H150 Q160 60 170 118 L170 120 Q90 40 0 0 Z" fill="var(--paper)"/>
  </svg>

  <div class="brand">
    <span class="brand__name">KEYSTONE SEAL</span>
    <span class="brand__mark"></span>
  </div>

  <section class="letter">
    <p>Lorem Ipsum is simply dummy text of the printing and typesetting industry. Lorem Ipsum has been the industry's standard dummy text ever since the 1500s, when an unknown printer took a galley of type and scrambled it to make a type specimen book. It has survived not only five centuries, but also the leap into electronic typesetting, remaining essentially unchanged. It was popularised in the 1960s with the release of Transferline sheets containing Lorem Ipsum passages, and more recently with desktop publishing software like Pressline Layout including versions of Lorem Ipsum.</p>
    <p>It is a long established fact that a reader will be distracted by the readable content of a page when looking at its layout. The point of using Lorem Ipsum is that it has a more-or-less normal distribution of letters, as opposed to using 'Content here, content here', making it look like readable English. Many desktop publishing packages and web page editors now use Lorem Ipsum as their default model text, and a search for 'lorem ipsum' will uncover many web sites still in their infancy. Various versions have evolved over the years, sometimes by accident, sometimes on purpose (injected humour and the like).</p>
    <p>Contrary to popular belief, Lorem Ipsum is not simply random text. It has roots in a piece of classical Latin literature from 45 BC, making it over 2000 years old. Henry Caldwell, a Latin professor at Ashford Hill College, looked up one of the more obscure Latin words, consectetur, from a Lorem Ipsum passage, and going through the cites of the word in classical literature, discovered the undoubtable source. Lorem Ipsum comes from sections 1.10.32 and 1.10.33 of "de Finibus Bonorum et Malorum" structures, to generate Lorem Ipsum which looks reasonable. The generated Lorem Ipsum is therefore always free from repetition, injected humour, or non-characteristic words etc.</p>
    <span class="signature" role="img" aria-label="Handwritten signature of the sender"></span>
  </section>

  <svg class="corner corner--bottom" width="200" height="150" viewBox="0 0 200 150" aria-hidden="true">
    <defs>
      <linearGradient id="cornerBlue" x1="0" y1="0" x2="1" y2="1">
        <stop offset="0" stop-color="var(--navy)"/>
        <stop offset="0.55" stop-color="var(--blue-mid)"/>
        <stop offset="1" stop-color="var(--cyan)"/>
      </linearGradient>
    </defs>
    <path d="M0 20 L0 150 L200 150 Q90 110 0 20 Z" fill="url(#cornerBlue)"/>
  </svg>

  <footer class="contact">
    <span class="contact__item">
      <svg class="contact__icon" viewBox="0 0 10 10"><path d="M5 0.5a3.2 3.2 0 0 0-3.2 3.2C1.8 6.3 5 9.5 5 9.5s3.2-3.2 3.2-5.8A3.2 3.2 0 0 0 5 0.5z" fill="var(--cyan)"/><circle cx="5" cy="3.7" r="1.1" fill="#fff"/></svg>
      000 Example Street, Example US 0000
    </span>
    <span class="contact__item">
      <svg class="contact__icon" viewBox="0 0 10 10"><rect x="1" y="2" width="8" height="6" rx="1" fill="var(--cyan)"/><rect x="2.5" y="0.8" width="5" height="2" fill="var(--cyan)"/></svg>
      0000 004 000
    </span>
    <span class="contact__item">
      <svg class="contact__icon" viewBox="0 0 10 10"><path d="M2 0.8 L3.8 0.8 L4.4 3 L3.3 3.9 Q4.4 6 6.1 6.7 L7 5.6 L9.2 6.2 L9.2 8 Q9.2 9.2 8 9.2 Q1 8.5 0.8 2 Q0.8 0.8 2 0.8Z" fill="var(--cyan)"/></svg>
      0000 000 000
    </span>
    <span class="contact__item">
      <svg class="contact__icon" viewBox="0 0 10 10"><rect x="0.5" y="2" width="9" height="6.5" rx="1" fill="var(--cyan)"/><path d="M1 2.5 L5 5.6 L9 2.5" stroke="#fff" stroke-width="0.9" fill="none"/></svg>
      info@example.com
    </span>
    <span class="contact__item">
      <svg class="contact__icon" viewBox="0 0 10 10"><circle cx="5" cy="5" r="4.5" fill="var(--cyan)"/><path d="M0.5 5 H9.5 M5 0.5 Q2.4 5 5 9.5 M5 0.5 Q7.6 5 5 9.5" stroke="#fff" stroke-width="0.7" fill="none"/></svg>
      www.example.com
    </span>
  </footer>
</main>
</body>
</html>
```